Postcard for dumpster rental business

We need an attractive post card to entice other businesses to use our dumpster rental service. This is a business to business situation.
Target Market(s)
Roofing, property restoration and remodeling contractors
Industry/Entity Type
Dumpster rentals
Font styles to use
Sans Serif
Colors
0054AA
0677BA
7BADD7
CADEEF
E8F1F8
Requirements
Must have
- tossbinhaul.com Dumpster rental Easy online booking Logo Guaranteed On Time Delivery (as a badge or button?) QR Code Picture of our dumpster (see website)
Nice to have
- Call to action "Order now!"

```html
<!DOCTYPE html>
<html lang="en">
<head>
<meta charset="utf-8">
<title>TossBin Haul Postcard</title>
<link href="https://fonts.googleapis.com/css2?family=Arimo:wght@400;700&family=Oswald:wght@500&display=swap" rel="stylesheet">
<style>
:root{
  --navy:#1b2a57;
  --navy-deep:#152147;
  --blue:#0054AA;
  --blue-mid:#0677BA;
  --blue-soft:#7BADD7;
  --blue-pale:#CADEEF;
  --blue-mist:#E8F1F8;
  --orange:#f26a21;
  --white:#ffffff;
  --ink:#1d1d1f;
  --page:#e6e8ec;
}
*{box-sizing:border-box;margin:0;padding:0}
html,body{width:1131px;height:1200px;overflow:hidden;background:var(--page);font-family:"Arimo",Arial,sans-serif}
.card{position:absolute;left:70px;width:990px;height:550px;background:var(--white);overflow:hidden;box-shadow:0 4px 14px rgba(0,0,0,.25)}
.card--front{top:30px}
.card--back{top:615px}
.abs{position:absolute}
.shapes{position:absolute;left:0;top:0}

/* front */
.hero-photo{left:455px;top:0;width:535px;height:373px;background:linear-gradient(160deg,#6d7f92 0%,#8a6a52 45%,#c9762f 75%,#7a5a40 100%)}
.brand{left:30px;top:26px;color:var(--white)}
.brand__name{display:flex;align-items:center;gap:8px;font-weight:700;font-size:30px;letter-spacing:.5px}
.brand__mark{width:22px;height:22px;background:var(--white)}
.brand__tag{font-weight:700;font-size:20px;letter-spacing:1px;margin-top:4px}
.brand__phone{font-weight:700;font-size:14px;letter-spacing:1px;margin-top:2px}
.headline{left:28px;top:142px;color:var(--white);font-weight:700;font-size:40px;line-height:46px;letter-spacing:.3px}
.lede{left:28px;top:292px;width:420px;color:var(--white);font-size:15px;line-height:20px}
.badge{left:432px;top:262px;width:100px;height:96px}
.bin{position:absolute;top:395px;width:230px}
.bin__photo{width:190px;height:62px;background:linear-gradient(180deg,#f07f2f,#d45a14);border-top:5px solid #c24f10}
.bin__price{position:absolute;left:150px;top:20px;width:48px;height:48px;border-radius:50%;background:var(--blue-mid);border:3px solid var(--white);box-shadow:0 1px 3px rgba(0,0,0,.3);color:var(--white);font-weight:700;font-size:15px;display:flex;align-items:center;justify-content:center}
.bin__price sup{font-size:8px}
.bin__specs{display:flex;gap:8px;margin-top:12px;margin-left:-22px;font-size:6px;line-height:7px;color:var(--ink)}
.spec{display:flex;gap:3px;align-items:center}
.spec b{display:block}
.spec i{display:block;width:14px;height:10px;background:var(--ink)}
.bar-left{left:0;top:511px;width:590px;height:39px;color:var(--white);font-weight:700;font-size:15px;letter-spacing:.5px;display:flex;align-items:center;gap:14px;padding-left:46px}
.bar-cta{color:var(--white);font-family:"Oswald","Arial Narrow",sans-serif;font-weight:500;display:flex;align-items:center;gap:10px}
.bar-cta--front{left:560px;top:502px;height:48px;padding-left:30px;font-size:19px}
.bar-cta big{font-size:23px}

/* back */
.site-photo{left:0;top:0;width:545px;height:160px;background:linear-gradient(180deg,#6f8fb5 0%,#c9c1ae 55%,#9b8d78 100%)}
.bin-photo{left:335px;top:90px;width:190px;height:80px;background:linear-gradient(180deg,#f07f2f,#d45a14)}
.take-title{left:30px;top:176px;color:var(--white);font-weight:700;font-size:24px;letter-spacing:.4px}
.checklist{left:30px;top:228px;display:grid;grid-template-columns:248px 250px;row-gap:8px;color:var(--white);font-size:15.5px;list-style:none}
.checklist li{display:flex;align-items:center;gap:8px}
.about{left:30px;top:398px;width:505px;color:var(--white);font-size:12px;line-height:14px}
.bar-cta--back{left:0;top:465px;height:46px;padding-left:22px;font-size:19px}
.back-foot{left:18px;top:518px;color:var(--navy);font-weight:700;font-size:15px;letter-spacing:.5px;display:flex;align-items:center;gap:14px}
.brand--back{left:555px;top:36px;color:var(--blue);text-align:center}
.brand--back .brand__mark{background:var(--blue)}
.stamp{left:850px;top:33px;width:115px;height:115px;border:1px solid #c8c8c8}
.address-line{left:610px;width:355px;height:1px;background:#c8c8c8}
</style>
</head>
<body>

<section class="card card--front">
  <div class="abs hero-photo" role="img" aria-label="Photo of a worker tossing debris into an orange roll-off dumpster in front of a house under renovation"></div>
  <svg class="shapes" width="990" height="550" viewBox="0 0 990 550" aria-hidden="true">
    <defs>
      <linearGradient id="panel" x1="0" y1="0" x2="0" y2="1">
        <stop offset="0" stop-color="#2478c4"/><stop offset=".55" stop-color="#1d3f7c"/><stop offset="1" stop-color="#1b2a57"/>
      </linearGradient>
    </defs>
    <polygon points="0,0 575,0 490,180 575,373 0,373" fill="#0677BA"/>
    <polygon points="0,0 560,0 475,180 560,373 0,373" fill="url(#panel)"/>
    <rect x="0" y="373" width="990" height="138" fill="#f4f7fa"/>
    <polygon points="0,373 75,373 0,520" fill="#0677BA"/>
    <polygon points="75,373 110,373 20,520 0,520 0,500" fill="#7BADD7"/>
    <rect x="0" y="511" width="990" height="39" fill="#1b2a57"/>
  </svg>

  <div class="abs brand">
    <div class="brand__name"><span class="brand__mark"></span>TOSSBIN HAUL</div>
    <div class="brand__tag">DUMPSTER RENTAL</div>
    <div class="brand__phone">(555) 014-2287</div>
  </div>
  <h1 class="abs headline">DUMPSTER RENTAL<br>AND REMOVAL<br>SERVICES</h1>
  <p class="abs lede">We provide fast, friendly services in Wayne, Oakland, and Macomb County Communities.</p>

  <svg class="abs badge" viewBox="0 0 100 96" aria-label="On-time delivery badge">
    <polygon points="50,2 94,26 94,70 50,94 6,70 6,26" fill="#0677BA"/>
    <polygon points="50,10 87,30 87,66 50,86 13,66 13,30" fill="#ffffff"/>
    <polygon points="50,16 81,33 81,63 50,80 19,63 19,33" fill="#1b2a57"/>
    <rect x="8" y="36" width="84" height="26" fill="#ffffff"/>
    <text x="50" y="47" text-anchor="middle" font-family="Arimo,Arial,sans-serif" font-weight="700" font-size="11" fill="#1b2a57">ON-TIME</text>
    <text x="50" y="59" text-anchor="middle" font-family="Arimo,Arial,sans-serif" font-weight="700" font-size="11" fill="#1b2a57">DELIVERY</text>
    <g fill="#ffffff"><circle cx="42" cy="28" r="2"/><circle cx="50" cy="25" r="2.4"/><circle cx="58" cy="28" r="2"/><circle cx="50" cy="71" r="2.4"/></g>
  </svg>

  <div class="bin" style="left:145px">
    <div class="bin__photo" role="img" aria-label="Orange 14 foot roll-off dumpster"></div>
    <div class="bin__price"><sup>$</sup>318</div>
    <div class="bin__specs">
      <div class="spec"><i></i><span><b>DIMENSIONS</b>14' L X 7' W X 2.5' H</span></div>
      <div class="spec"><i></i><span><b>RENTAL TIME</b>UP TO 5 DAYS</span></div>
      <div class="spec"><i></i><span><b>INCLUDED TONNAGE</b>2 INCLUDED</span></div>
    </div>
  </div>
  <div class="bin" style="left:450px">
    <div class="bin__photo" role="img" aria-label="Orange 16 foot roll-off dumpster"></div>
    <div class="bin__price"><sup>$</sup>358</div>
    <div class="bin__specs">
      <div class="spec"><i></i><span><b>DIMENSIONS</b>16' L X 7' W X 3.5' H</span></div>
      <div class="spec"><i></i><span><b>RENTAL TIME</b>UP TO 5 DAYS</span></div>
      <div class="spec"><i></i><span><b>INCLUDED TONNAGE</b>2.5 INCLUDED</span></div>
    </div>
  </div>
  <div class="bin" style="left:752px">
    <div class="bin__photo" role="img" aria-label="Orange 16 foot tall roll-off dumpster"></div>
    <div class="bin__price"><sup>$</sup>398</div>
    <div class="bin__specs">
      <div class="spec"><i></i><span><b>DIMENSIONS</b>16' L X 7' W X 5' H</span></div>
      <div class="spec"><i></i><span><b>RENTAL TIME</b>UP TO 5 DAYS</span></div>
      <div class="spec"><i></i><span><b>INCLUDED TONNAGE</b>3 INCLUDED</span></div>
    </div>
  </div>

  <div class="abs bar-left">
    <span>EASY ONLINE BOOKING</span>
    <svg width="16" height="16" viewBox="0 0 16 16" aria-hidden="true"><g fill="none" stroke="#fff" stroke-width="1.3"><circle cx="8" cy="8" r="6.5"/><ellipse cx="8" cy="8" rx="3" ry="6.5"/><path d="M1.5 8h13"/></g></svg>
    <span>TOSSBINHAUL.COM</span>
  </div>
  <svg class="abs" style="left:560px;top:502px" width="430" height="48" aria-hidden="true"><polygon points="18,0 430,0 430,48 0,48" fill="#f26a21"/></svg>
  <div class="abs bar-cta bar-cta--front">
    <span>CALL TODAY FOR FREE QUOTE</span>
    <svg width="18" height="20" viewBox="0 0 18 20" aria-hidden="true"><path d="M3 1h5l1 5-3 2q2 4 5 6l2-3 5 1v5q-1 2-3 2Q5 18 1 4q0-2 2-3z" fill="#fff"/></svg>
    <big>(555) 014-2287</big>
  </div>
</section>

<section class="card card--back">
  <svg class="shapes" width="990" height="550" viewBox="0 0 990 550" aria-hidden="true">
    <defs>
      <linearGradient id="backpanel" x1="0" y1="0" x2="0" y2="1">
        <stop offset="0" stop-color="#1b2a57"/><stop offset=".4" stop-color="#1d4f8f"/><stop offset="1" stop-color="#1b2a57"/>
      </linearGradient>
    </defs>
    <polygon points="0,0 512,0 562,268 512,550 0,550" fill="#0677BA"/>
    <polygon points="0,0 500,0 550,268 500,550 0,550" fill="url(#backpanel)"/>
    <rect x="0" y="165" width="520" height="50" fill="#1b2a57"/>
    <rect x="0" y="505" width="520" height="45" fill="#ffffff"/>
    <polygon points="500,505 520,505 512,550 500,550" fill="#ffffff"/>
  </svg>
  <div class="abs site-photo" role="img" aria-label="Photo of new townhomes under construction"></div>
  <div class="abs bin-photo" role="img" aria-label="Orange roll-off dumpster filled with debris"></div>
  <h2 class="abs take-title">WE TAKE JUST ABOUT EVERYTHING</h2>
  <ul class="abs checklist">
    <li><svg width="14" height="14" viewBox="0 0 14 14" aria-hidden="true"><rect x=".5" y=".5" width="13" height="13" fill="#fff"/><path d="M3 7l3 3 5-6" stroke="#f26a21" stroke-width="2" fill="none"/></svg>Refrigerator Disposal</li>
    <li><svg width="14" height="14" viewBox="0 0 14 14" aria-hidden="true"><rect x=".5" y=".5" width="13" height="13" fill="#fff"/><path d="M3 7l3 3 5-6" stroke="#f26a21" stroke-width="2" fill="none"/></svg>Trash Removal</li>
    <li><svg width="14" height="14" viewBox="0 0 14 14" aria-hidden="true"><rect x=".5" y=".5" width="13" height="13" fill="#fff"/><path d="M3 7l3 3 5-6" stroke="#f26a21" stroke-width="2" fill="none"/></svg>Garbage Removal</li>
    <li><svg width="14" height="14" viewBox="0 0 14 14" aria-hidden="true"><rect x=".5" y=".5" width="13" height="13" fill="#fff"/><path d="M3 7l3 3 5-6" stroke="#f26a21" stroke-width="2" fill="none"/></svg>Appliance Removal</li>
    <li><svg width="14" height="14" viewBox="0 0 14 14" aria-hidden="true"><rect x=".5" y=".5" width="13" height="13" fill="#fff"/><path d="M3 7l3 3 5-6" stroke="#f26a21" stroke-width="2" fill="none"/></svg>Mattress Disposal</li>
    <li><svg width="14" height="14" viewBox="0 0 14 14" aria-hidden="true"><rect x=".5" y=".5" width="13" height="13" fill="#fff"/><path d="M3 7l3 3 5-6" stroke="#f26a21" stroke-width="2" fill="none"/></svg>Television Disposal &amp; Recycling</li>
    <li><svg width="14" height="14" viewBox="0 0 14 14" aria-hidden="true"><rect x=".5" y=".5" width="13" height="13" fill="#fff"/><path d="M3 7l3 3 5-6" stroke="#f26a21" stroke-width="2" fill="none"/></svg>Foreclosure Clean Outs</li>
    <li><svg width="14" height="14" viewBox="0 0 14 14" aria-hidden="true"><rect x=".5" y=".5" width="13" height="13" fill="#fff"/><path d="M3 7l3 3 5-6" stroke="#f26a21" stroke-width="2" fill="none"/></svg>Furniture Removal</li>
    <li><svg width="14" height="14" viewBox="0 0 14 14" aria-hidden="true"><rect x=".5" y=".5" width="13" height="13" fill="#fff"/><path d="M3 7l3 3 5-6" stroke="#f26a21" stroke-width="2" fill="none"/></svg>Construction Waste Removal</li>
    <li><svg width="14" height="14" viewBox="0 0 14 14" aria-hidden="true"><rect x=".5" y=".5" width="13" height="13" fill="#fff"/><path d="M3 7l3 3 5-6" stroke="#f26a21" stroke-width="2" fill="none"/></svg>E-Waste Disposal</li>
    <li><svg width="14" height="14" viewBox="0 0 14 14" aria-hidden="true"><rect x=".5" y=".5" width="13" height="13" fill="#fff"/><path d="M3 7l3 3 5-6" stroke="#f26a21" stroke-width="2" fill="none"/></svg>Yard Waste Removal</li>
    <li><svg width="14" height="14" viewBox="0 0 14 14" aria-hidden="true"><rect x=".5" y=".5" width="13" height="13" fill="#fff"/><path d="M3 7l3 3 5-6" stroke="#f26a21" stroke-width="2" fill="none"/></svg>Hot Tub Disposal</li>
  </ul>
  <p class="abs about">TossBin Haul Dumpster Rental is locally owned and operated by a small-business team with a reputation that spans over 30 years. Our competitive prices and high standards allow us to offer comprehensive, professional, and personalized customer-service to meet your practical and financial needs.</p>
  <svg class="abs" style="left:0;top:465px" width="435" height="46" aria-hidden="true"><polygon points="0,0 415,0 435,46 0,46" fill="#f26a21"/></svg>
  <div class="abs bar-cta bar-cta--back">
    <span>CALL TODAY FOR FREE QUOTE</span>
    <svg width="18" height="20" viewBox="0 0 18 20" aria-hidden="true"><path d="M3 1h5l1 5-3 2q2 4 5 6l2-3 5 1v5q-1 2-3 2Q5 18 1 4q0-2 2-3z" fill="#fff"/></svg>
    <big>(555) 014-2287</big>
  </div>
  <div class="abs back-foot">
    <span>EASY ONLINE BOOKING</span>
    <svg width="16" height="16" viewBox="0 0 16 16" aria-hidden="true"><g fill="none" stroke="#1b2a57" stroke-width="1.3"><circle cx="8" cy="8" r="6.5"/><ellipse cx="8" cy="8" rx="3" ry="6.5"/><path d="M1.5 8h13"/></g></svg>
    <span>TOSSBINHAUL.COM</span>
  </div>

  <div class="abs brand brand--back">
    <div class="brand__name"><span class="brand__mark"></span>TOSSBIN HAUL</div>
    <div class="brand__tag">DUMPSTER RENTAL</div>
    <div class="brand__phone">(555) 014-2287</div>
  </div>
  <div class="abs stamp"></div>
  <div class="abs address-line" style="top:228px"></div>
  <div class="abs address-line" style="top:275px"></div>
  <div class="abs address-line" style="top:320px"></div>
  <div class="abs address-line" style="top:365px"></div>
</section>

</body>
</html>
```